VESTRA電子書籍 表紙発注書

【依頼概要】

<サブタイトル>

小さな会社や個人事業でもできる!

<書籍タイトル>

数字が苦手な 店主のための
【看板づくり手帖】

※ターゲットの目にすぐ入る様に(小さな会社)(個人事業)(ネットに弱い)を目立つ様にお願いします。
※電子書籍なので表示される際の画像が小さいため、タイトルもできるだけ視認しやすい文字でお願いします。

<オビ部分>

ホームページを作る前に
必ずお読みください。

読者限定プレゼント付
●思わずポチッと押したくなる!
【段階別】キャッチコピーの作り方
●真似するだけでOK!
【ランディングページのテンプレート】

※プレゼントは目立つ様にお願いします。

<著者>

WEB集客のしくみ作りの専門家
森田 サキ

※著者似顔絵をどちらか使ってください。

<読者ターゲット層>
・40代~50代の、小規模企業の経営者・個人事業経営者・個人起業家

<イメージ>
・色の指定などはありません。
もし自分が起業する時なら、どんな表紙に目が止まるか考えてみていただけると嬉しいです。

・ビジネス書ではありますが、ターゲットはネットやパソコンに苦手意識を持っている経営者の方なので、また女性の起業家さんにも見て欲しいので、ちゃんとした雰囲気はありつつも、あまり硬くなく、自分でもできそうかなー、と思わせる様な雰囲気が出るといいなと思っています。
よろしくお願いいたします。

※著者似顔絵2点添付します。どちらかをお使いください。
※写真・イラスト素材購入の際は別途お支払いします。 その場合は、小サイズ画像で大丈夫です。

※参考資料として、まだ未完成ですが原稿を添付します。
パスワードがありますのでこちらで開いてください。

▶︎PDFを開く時のパスワード: demo1

《追記1》必ずご覧ください。
↓ ↓ ↓
書籍のタイトルとオビの文言をを変更しました。
申し訳ありませんが、こちらを必ずご確認ください。

(すでに提案をくださった方は、そのままのデザインで検討させていただきますので、再提出はしなくて大丈夫です。採用になった場合のみ変更のご依頼をさせていただきますが、その際は報酬をプラスさせていただきます※9/15日朝7時30分までに提案くださった方)

《変更内容》
<書籍タイトル>
帳簿が苦手な 店主のための
「街角で商売」

※ターゲットの目にすぐ入る様に(小さな会社)(個人事業)(ウェブに弱い)を目立つ様にお願いします。

<オビ部分>
※この本を読むまでは
ホームページは作らないでください。

▶︎参考本文(未完成)は新しい方(ファイル名:【原稿】こちらをご覧ください)
をご覧ください」
▶︎▶︎PDFファイルパスワード demo2
《追記2》
追記1にて一部変更をさせていただきましたが、
追記1の《変更内容》以外は最初の依頼内容通りなので、再度ご確認ください。

あと、少し気になったのですが、著者の似顔絵はメインビジュアルに使わなくて大丈夫です。名前の横にひっそりとつかう程度でいいかと思います。
もちろん、何か意図を持って使いたいという場合はご提案大歓迎です^ ^

▶︎必要な構成要素を再度まとめますね。
(読者ターゲットや希望デザインについては最初の依頼内容をご確認ください)
ーーーーーーーーーーーーーーーーーーー
<文字>
小さな会社や個人事業でもできる!

帳簿が苦手な 店主のための
「街角で商売」

※この本を読むまでは
ホームページは作らないでください。

読者限定プレゼント付
●思わずポチッと押したくなる!
【段階別 キャッチコピーの作り方】
●真似するだけでOK!
【ランディングページのテンプレート】

WEB集客のしくみ作りの専門家
森田 サキ

<画像>
著者似顔絵(メインビジュアルには使わなくていいいです)

※その他、写真・イラストの使用はお任せ

ーーーーーーーーーーーーーーーーーーー

こちらの説明不足のため誤解を招いてしまい、たいへん申し訳ございませんでした。

誰のための何の本ななのか、スマホでVestraを見た時でもはっきりわかるスッキリしたデザインがよかったです。また、こちらの要望通りに、ウェブが苦手な人や女性も、ついポチッと押してしまいそうなデザインでした。

選考には、20人ほどの方から意見をいただいたのですが、やはりはっきり文字が読み取れるものが人気が高かったです。
なるほどなぁ、と思ったのは、少しデザインの知識がある人(私を含め)と、とくにこだわりのない普通の人たちとでは、見る視点が違うのか、少し意見が別れました。読者目線がやはり大事ですね。

たくさんのご提案をいただき、本当にありがとうございました。

中には、さすがプロっぽいと思わせる作品や、手間をかけて作ってくださったと思われる作品もあり、本当にありがたく、また選考もかなり迷いました。

提案してくださった皆様、本当にありがとうございました。

```html
<!DOCTYPE html>
<html lang="ja">
<head>
<meta charset="utf-8">
<title>帳簿が苦手な店主のための 街角で商売</title>
<link href="https://fonts.googleapis.com/css2?family=Noto+Sans+JP:wght@500;700;900&display=swap" rel="stylesheet">
<style>
  :root {
    --sky: #86c8ec;
    --sky-light: #b5def4;
    --navy: #1d2f6b;
    --yellow: #fbe94a;
    --red: #e0283a;
    --pink: #f7dbe4;
    --white: #ffffff;
    --ink: #111111;
  }
  html, body { margin: 0; padding: 0; overflow: hidden; background: #ffffff; }
  .cover {
    position: relative;
    width: 750px;
    height: 1200px;
    overflow: hidden;
    font-family: "Noto Sans JP", sans-serif;
    background: linear-gradient(180deg, var(--sky-light) 0%, var(--sky) 60%);
    color: var(--navy);
  }
  .subtitle {
    position: absolute;
    left: 16px;
    top: 26px;
    height: 770px;
    writing-mode: vertical-rl;
    white-space: nowrap;
    font-weight: 900;
    font-size: 52px;
    line-height: 1;
    color: var(--navy);
    text-shadow: 0 0 4px #fff, 0 0 4px #fff;
  }
  .subtitle small { font-size: 32px; }
  .title-lead {
    position: absolute;
    margin: 0;
    left: 96px;
    top: 24px;
    width: 640px;
    text-align: center;
    font-weight: 900;
    font-size: 80px;
    line-height: 1.1;
    color: var(--navy);
    text-shadow: 3px 3px 0 #fff, -3px 3px 0 #fff, 3px -3px 0 #fff, -3px -3px 0 #fff;
  }
  .title-main {
    position: absolute;
    left: 112px;
    top: 240px;
    width: 508px;
    height: 350px;
    background: var(--yellow);
    border-radius: 8px;
  }
  .title-main svg { position: absolute; inset: 0; }
  .title-main p {
    position: absolute;
    margin: 0;
    font-weight: 900;
    color: var(--navy);
    line-height: 1;
    white-space: nowrap;
  }
  .title-main .line1 { left: 0; right: 0; text-align: center; top: 30px; font-size: 132px; }
  .title-main .line2 { left: 50px; top: 184px; font-size: 140px; letter-spacing: 0.06em; }
  .author-portrait {
    position: absolute;
    left: 590px;
    top: 420px;
    width: 145px;
    height: 165px;
    border-radius: 50% 50% 10px 10px;
    background: linear-gradient(180deg, #f5d6c4 0%, #e39aa6 100%);
  }
  .notice {
    position: absolute;
    left: 140px;
    top: 630px;
    width: 420px;
    height: 140px;
    background: var(--white);
    border: 4px solid var(--ink);
    border-radius: 34px;
    box-sizing: border-box;
    display: flex;
    align-items: center;
    justify-content: center;
    text-align: center;
    font-weight: 900;
    font-size: 33px;
    line-height: 1.25;
    color: var(--ink);
  }
  .notice-tail { position: absolute; left: 554px; top: 660px; }
  .author-role {
    position: absolute;
    left: 578px;
    top: 596px;
    width: 165px;
    font-weight: 700;
    font-size: 20px;
    line-height: 1.2;
    color: var(--navy);
  }
  .author-name {
    position: absolute;
    left: 576px;
    top: 672px;
    font-weight: 900;
    font-size: 34px;
    line-height: 1.2;
    color: var(--navy);
    white-space: nowrap;
  }
  .gift-band {
    position: absolute;
    left: 0;
    top: 800px;
    width: 750px;
    height: 400px;
    background: var(--pink);
  }
  .gift-badge {
    position: absolute;
    left: 16px;
    top: 820px;
    width: 180px;
    height: 165px;
    background: var(--red);
    color: var(--white);
    border-radius: 10px;
    transform: rotate(-7deg);
    display: flex;
    align-items: center;
    justify-content: center;
    text-align: center;
    font-weight: 900;
    font-size: 34px;
    line-height: 1.25;
    border: 4px solid var(--white);
    box-shadow: 0 3px 0 rgba(0,0,0,0.15);
  }
  .gift-item { position: absolute; left: 228px; width: 510px; text-align: center; }
  .gift-item .hook {
    display: inline-block;
    background: var(--navy);
    color: var(--yellow);
    font-weight: 700;
    font-size: 23px;
    padding: 2px 16px;
    border-radius: 4px;
  }
  .gift-item .name {
    margin: 6px 0 0;
    font-weight: 900;
    font-size: 46px;
    line-height: 1.15;
    color: var(--navy);
  }
  .gift-item .tag {
    display: inline-block;
    vertical-align: middle;
    background: var(--red);
    color: var(--white);
    font-size: 20px;
    font-weight: 700;
    padding: 2px 6px;
    margin-right: 8px;
    border-radius: 3px;
  }
  .gift-one { top: 812px; }
  .gift-two { top: 990px; }
  .divider { position: absolute; left: 240px; top: 975px; width: 490px; border-top: 3px dashed var(--navy); opacity: 0.4; }
</style>
</head>
<body>
<div class="cover">
  <div class="subtitle">小さな会社<small>や</small>個人事業<small>でも</small>できる!</div>

  <h1 class="title-lead">帳簿が苦手な<br>店主のための</h1>

  <div class="title-main">
    <svg width="508" height="350" viewBox="0 0 508 350" aria-hidden="true">
      <path d="M34 22 H12 V328 H34" fill="none" stroke="var(--red)" stroke-width="9"/>
      <path d="M474 22 H496 V328 H474" fill="none" stroke="var(--red)" stroke-width="9"/>
    </svg>
    <p class="line1">街角で</p>
    <p class="line2">商売</p>
  </div>

  <div class="author-portrait" role="img" aria-label="著者の似顔絵イラスト"></div>

  <div class="notice">この本を読むまでは<br>ホームページは<br>作らないでください。</div>
  <svg class="notice-tail" width="26" height="36" viewBox="0 0 26 36" aria-hidden="true">
    <path d="M0 4 L22 18 L0 32" fill="var(--white)" stroke="var(--ink)" stroke-width="4" stroke-linejoin="round"/>
    <rect x="0" y="7" width="5" height="22" fill="var(--white)"/>
  </svg>

  <div class="author-role">WEB集客の<br>しくみ作りの<br>専門家</div>
  <div class="author-name">森田 サキ</div>

  <div class="gift-band"></div>
  <div class="gift-badge">読者限定<br>プレゼント<br>付き</div>

  <div class="gift-item gift-one">
    <span class="hook">思わずポチッと押したくなる!</span>
    <p class="name"><span class="tag">段階別</span>キャッチコピーの<br>作り方</p>
  </div>
  <div class="divider"></div>
  <div class="gift-item gift-two">
    <span class="hook">真似するだけでOK!</span>
    <p class="name">ランディングページの<br>テンプレート</p>
  </div>
</div>
</body>
</html>
```